Water ATM Card

Need a design for water ATM cards. Size of card is 3.375 x 2.125 inch
On the Front include the Cedar Brook Logo.
Bottom right corner should have Price $100
On the Back
This card is to be used to access water refills at any Cedar Brook Water Vending Machines.
Please contact (869) 415 2983 or (869) 238 4617 or email clearflowhub@mailbox-example.com for any assistance or recharging of card.

```html
<!DOCTYPE html>
<html lang="en">
<head>
<meta charset="utf-8">
<title>Cedar Brook Water ATM Card</title>
<link rel="stylesheet" href="https://fonts.googleapis.com/css2?family=Montserrat:wght@700&family=Open+Sans:wght@400;700&display=swap">
<style>
  :root {
    --backdrop: #a3a7a8;
    --card: #ffffff;
    --brand-blue: #1a73b9;
    --price-blue: #2d83c5;
    --band-blue: #2a88cc;
    --icon-blue: #2f6fb5;
    --ink: #333333;
  }
  html, body {
    margin: 0;
    width: 1179px;
    height: 1200px;
    overflow: hidden;
    background: var(--backdrop);
  }
  .sheet {
    position: relative;
    width: 1179px;
    height: 1200px;
  }
  .card {
    position: absolute;
    left: 231px;
    width: 717px;
    height: 452px;
    background: var(--card);
    border-radius: 28px;
    overflow: hidden;
    box-shadow: 0 4px 14px rgba(0,0,0,0.45);
  }
  .card--front { top: 128px; }
  .card--back { top: 618px; }
  .brand {
    position: absolute;
    left: 0;
    right: 0;
    top: 120px;
    display: flex;
    justify-content: center;
    align-items: center;
    gap: 16px;
  }
  .brand__dot {
    width: 34px;
    height: 34px;
    border-radius: 50%;
    background: var(--brand-blue);
  }
  .brand__name {
    font-family: 'Montserrat', sans-serif;
    font-weight: 700;
    font-size: 50px;
    letter-spacing: 1px;
    color: var(--brand-blue);
    line-height: 1;
  }
  .price {
    position: absolute;
    right: 27px;
    top: 392px;
    font-family: 'Open Sans', sans-serif;
    font-weight: 700;
    font-size: 36px;
    color: var(--price-blue);
    line-height: 1;
  }
  .contacts {
    position: absolute;
    left: 0;
    right: 0;
    top: 398px;
    display: flex;
    justify-content: center;
    align-items: center;
    gap: 10px;
    font-family: 'Open Sans', sans-serif;
    font-size: 16.5px;
    color: var(--ink);
    white-space: nowrap;
  }
  .contact {
    display: flex;
    align-items: center;
    gap: 7px;
  }
  .contact svg { width: 20px; height: 16px; fill: var(--icon-blue); }
  .band {
    position: absolute;
    left: 0;
    right: 0;
    bottom: 0;
    height: 14px;
    background: var(--band-blue);
  }
</style>
</head>
<body>
<main class="sheet">
  <section class="card card--front" aria-label="Card front">
    <div class="brand">
      <span class="brand__dot"></span>
      <span class="brand__name">Cedar Brook</span>
    </div>
    <div class="price">Price $100</div>
  </section>

  <section class="card card--back" aria-label="Card back">
    <div class="brand">
      <span class="brand__dot"></span>
      <span class="brand__name">Cedar Brook</span>
    </div>
    <div class="contacts">
      <span class="contact">
        <svg viewBox="0 0 20 16" aria-hidden="true"><path d="M1 6c0-3 4-5 9-5s9 2 9 5v2h-5V5.5H6V8H1z"/><path d="M5 9l2-3h6l2 3v6H5z"/></svg>
        (869) 415 2983
      </span>
      <span class="contact">
        <svg viewBox="0 0 20 16" aria-hidden="true"><path d="M1 6c0-3 4-5 9-5s9 2 9 5v2h-5V5.5H6V8H1z"/><path d="M5 9l2-3h6l2 3v6H5z"/></svg>
        (869) 238 4617
      </span>
      <span class="contact">
        <svg viewBox="0 0 20 16" aria-hidden="true"><path d="M2 6l8-5 8 5v9H2z M4 7l6 4 6-4v7H4z" fill-rule="evenodd"/></svg>
        clearflowhub@mailbox-example.com
      </span>
    </div>
    <div class="band"></div>
  </section>
</main>
</body>
</html>
```